Income Tax Flyer - Updates Needed

Just need to update this flyer design and give it a new look. We would like to keep all the same wording but make it stand out a little more. Our selling point is the "Same Day Tax Advance up to $6,000"

Industry/Entity Type

Lending, Small Loans, Tax Services, Title Loans, Personal Loans

```html
<!DOCTYPE html>
<html lang="en">
<head>
<meta charset="utf-8">
<title>Keystone Lending Group – Tax Advance Flyer</title>
<link href="https://fonts.googleapis.com/css2?family=Outfit:wght@300;400;500;600;700&display=swap" rel="stylesheet">
<style>
  :root {
    --brand-green: #0b5132;
    --deep-green: #06331f;
    --brand-red: #c12127;
    --cream: #fdebd0;
    --ink: #1d1d1d;
    --paper: #ffffff;
    --backdrop: #e9e9e9;
  }
  * { margin: 0; padding: 0; box-sizing: border-box; }
  html, body {
    width: 1056px; height: 1200px; overflow: hidden;
    background: var(--backdrop);
    font-family: "Outfit", sans-serif;
  }
  .stage { position: relative; width: 1056px; height: 1200px; }
  .flyer {
    position: absolute; left: 157px; top: 30px;
    width: 977px; height: 1500px;
    background: var(--paper);
    transform: scale(0.76); transform-origin: top left;
    overflow: hidden;
  }
  .flyer-art { position: absolute; inset: 0; width: 977px; height: 1500px; }
  .brand {
    position: absolute; top: 110px; left: 0; width: 100%;
    text-align: center; color: var(--brand-green);
    font-size: 44px; font-weight: 600; letter-spacing: 0.5px;
  }
  .headline { position: absolute; left: 98px; top: 388px; color: #fff; font-weight: 700; }
  .headline-lead { font-size: 82px; line-height: 1; letter-spacing: -1px; }
  .headline-amount { font-size: 104px; line-height: 1; color: var(--cream); letter-spacing: -3px; margin-top: 22px; margin-left: -4px; }
  .headline-close { font-size: 106px; line-height: 1; margin-top: 14px; margin-left: -4px; }
  .pitch {
    position: absolute; left: 95px; top: 838px;
    font-size: 52px; font-weight: 700; line-height: 61px;
    color: var(--brand-green); letter-spacing: -0.5px;
  }
  .pitch-accent { color: var(--brand-red); }
  .benefit {
    position: absolute; top: 1080px; height: 86px;
    border-left: 3px solid var(--brand-red);
  }
  .benefit svg { position: absolute; left: 14px; top: 0; }
  .benefit-text {
    position: absolute; top: 12px;
    font-size: 19px; font-weight: 500; line-height: 27px;
    color: var(--ink); white-space: nowrap;
  }
  .cta {
    position: absolute; left: 95px; top: 1238px;
    width: 348px; height: 62px; border-radius: 31px;
    background: var(--brand-green); color: #fff;
    font-size: 29px; font-weight: 500;
    display: flex; align-items: center; justify-content: center;
  }
  .phone {
    position: absolute; left: 487px; top: 1250px;
    font-size: 30px; font-weight: 600; color: var(--brand-red);
  }
  .locations { position: absolute; left: 93px; top: 1328px; list-style: none; }
  .location {
    display: flex; align-items: center; height: 30.5px;
    font-size: 22px; font-weight: 300; letter-spacing: 1px; color: var(--ink);
  }
  .location svg { margin-right: 22px; flex: none; }
</style>
</head>
<body>
<div class="stage">
  <div class="flyer">
    <svg class="flyer-art" viewBox="0 0 977 1500" aria-hidden="false">
      <path d="M0,425 Q488,42 977,410 L977,1165 C750,880 350,750 0,797 Z" fill="var(--brand-red)"/>
      <defs>
        <linearGradient id="photoTone" x1="0" y1="0" x2="1" y2="1">
          <stop offset="0" stop-color="#0b5a35"/>
          <stop offset="0.6" stop-color="#0a4a2c"/>
          <stop offset="1" stop-color="#05301c"/>
        </linearGradient>
      </defs>
      <path role="img" aria-label="Photo of a young couple reviewing paperwork together, tinted green"
            d="M0,440 Q488,140 977,420 L977,1150 C720,820 330,690 0,795 Z" fill="url(#photoTone)"/>
    </svg>

    <div class="brand">Keystone Lending Group</div>

    <div class="headline">
      <div class="headline-lead">APPLY HERE FOR</div>
      <div class="headline-amount">$5,000-$6,000</div>
      <div class="headline-close">TODAY!</div>
    </div>

    <div class="pitch">
      File your taxes<br>
      and apply for an<br>
      <span class="pitch-accent">Easy Advance!</span>
    </div>

    <div class="benefit" style="left:96px">
      <svg width="92" height="92" viewBox="0 0 92 92" fill="none" stroke="var(--brand-green)" stroke-width="2.5">
        <circle cx="38" cy="36" r="34" stroke-dasharray="3 6"/>
        <path d="M38 10 V36 L48 46"/>
        <rect x="30" y="56" width="56" height="28" rx="2" fill="#fff"/>
        <text x="58" y="77" font-family="Outfit, sans-serif" font-size="20" font-weight="600" fill="var(--brand-green)" stroke="none" text-anchor="middle">$</text>
        <circle cx="42" cy="70" r="3"/><circle cx="74" cy="70" r="3"/>
      </svg>
      <div class="benefit-text" style="left:112px">Available in<br>24 Hours or less</div>
    </div>

    <div class="benefit" style="left:376px">
      <svg width="110" height="110" viewBox="0 0 110 110" fill="none" stroke="var(--brand-green)" stroke-width="2.5">
        <circle cx="40" cy="34" r="33"/>
        <text x="40" y="47" font-family="Outfit, sans-serif" font-size="36" font-weight="500" fill="var(--brand-green)" stroke="none" text-anchor="middle">$</text>
        <path d="M52 56 L56 70 L62 62 L90 70 L100 82 L86 100 L70 90 L56 84 Z" fill="#fff"/>
      </svg>
      <div class="benefit-text" style="left:106px">Choose Your<br>Loan Amount</div>
    </div>

    <div class="benefit" style="left:648px">
      <svg width="110" height="80" viewBox="0 0 110 80" fill="none" stroke="var(--brand-green)" stroke-width="2.5">
        <path d="M8 18 H36 M2 30 H30 M10 42 H28 M2 54 H30 M8 66 H36"/>
        <circle cx="70" cy="37" r="33"/>
        <circle cx="70" cy="37" r="24"/>
        <text x="70" y="50" font-family="Outfit, sans-serif" font-size="34" font-weight="500" fill="var(--brand-green)" stroke="none" text-anchor="middle">$</text>
      </svg>
      <div class="benefit-text" style="left:131px">Quick and<br>Easy</div>
    </div>

    <div class="cta">Contact Us Today!</div>
    <div class="phone">Phone Number</div>

    <ul class="locations">
      <li class="location">
        <svg width="20" height="26" viewBox="0 0 20 26"><path d="M10 0 A10 10 0 0 1 20 10 C20 17 10 26 10 26 C10 26 0 17 0 10 A10 10 0 0 1 10 0 Z" fill="#111"/><circle cx="10" cy="10" r="4" fill="#fff"/></svg>
        Suite 210 145 Cedar Ridge, Millbrook, AZ 58001
      </li>
      <li class="location">
        <svg width="20" height="26" viewBox="0 0 20 26"><path d="M10 0 A10 10 0 0 1 20 10 C20 17 10 26 10 26 C10 26 0 17 0 10 A10 10 0 0 1 10 0 Z" fill="#111"/><circle cx="10" cy="10" r="4" fill="#fff"/></svg>
        Suite 408 92 Harbor Lane, Pinecrest, ME 12004
      </li>
      <li class="location">
        <svg width="20" height="26" viewBox="0 0 20 26"><path d="M10 0 A10 10 0 0 1 20 10 C20 17 10 26 10 26 C10 26 0 17 0 10 A10 10 0 0 1 10 0 Z" fill="#111"/><circle cx="10" cy="10" r="4" fill="#fff"/></svg>
        5120 Alder Point Road, Westfield, WA 73200
      </li>
    </ul>
  </div>
</div>
</body>
</html>
```